Brightwave Youth Academy is to provide global summer programs in the United States through which students from the US and China share experiences, intensive learning, and each other’s cultures. The program seeks to more fully prepare both the US and Chinese students for their college education and future careers in this interdependent world. Chinese students are individually paired with US Students where they will reside US students' home for the period of the program.

Current website: Brightwave Youth Academy

Need to support both English and Chinese with different font.
Updates

Project Deadline Extended
Reason: Because of Thanksgiving Holidays.

Dear Designers,

In order to generate the best design, I uploaded some photos from our global summer program. Please check:

http://brightwaveyouthacademy.org/photos/

Doreen

My company Logo just added to the project.

Sorry for the late update.

Project Deadline Extended
Reason: Due to Thanksgiving holiday, I don't have enough time to provide feedback to all the designers. Doreen

Project Deadline Extended
Reason: Holiday season. Need more time for designer and myself.

Target Market(s)

Grade K to 12 students and their parents to sign up the global summer program. Majority audience are from China.

Industry/Entity Type

College

Font styles to use
Sans Serif

Colors
3277b5

Requirements
Must have
• You may check my current website for the summer program content
www.brightwaveyouthacademy.org
Check these two clips to see what service we provided.
http://www.vidplexo.com/watch?v=9kR3mq41bTz&feature=vidplexo.be
https://www.vidplexo.com/watch?v=W7d2HN5p8oJ

Company Logo are included in the attachment.

Some photos from summer program: http://brightwaveyouthacademy.org/photos/
The website should show the students one to one relationship.
The website should show homestay part.

I want Photo Slider on each page to share the fun activities.

Each program will be provide a video clip as a summery.

The website should support font of both English and Chinese. I like to see both Chinese and English on the same page instead of switch back and forth. I can add Chinese part later if you leave the room.

Nice to have
• I have a lot of paired pictures. I am wondering if I can use collage of photos as the background.

The design should be playful and fun!

```html
<!DOCTYPE html>
<html lang="en">
<head>
<meta charset="utf-8">
<title>Brightwave Youth Academy</title>
<link rel="stylesheet" href="https://fonts.googleapis.com/css2?family=Cabin:wght@500&family=Parisienne&family=Libre+Baskerville&display=swap">
<style>
  :root {
    --brand-blue: #3277b5;
    --tagline-blue: #2b5d95;
    --ink: #333333;
    --logo-ink: #3d3d3d;
    --hero-tint: #e6ecf5;
    --rule: #d4d4d4;
    --footer-bg: #252525;
    --footer-base: #1c1c1c;
    --footer-text: #b9b9b9;
    --white: #ffffff;
    --phone-orange: #e8841f;
  }
  * { margin: 0; padding: 0; box-sizing: border-box; }
  html, body { width: 1075px; height: 1200px; overflow: hidden; }
  body {
    position: relative;
    background: #fbfcfe;
    font-family: Arial, Helvetica, sans-serif;
    color: var(--ink);
  }
  .site-header {
    position: absolute; left: 0; top: 0; width: 1075px; height: 122px;
    background: linear-gradient(#ffffff, #f3f4f6);
  }
  .brand {
    position: absolute; left: 92px; top: 44px;
    display: flex; align-items: center; gap: 10px;
    font-family: "Cabin", sans-serif; font-weight: 500;
    font-size: 22px; color: var(--logo-ink); white-space: nowrap;
  }
  .brand-dot { width: 16px; height: 16px; border-radius: 50%; background: var(--brand-blue); }
  .tagline {
    position: absolute; right: 107px; top: 50px;
    font-family: "Parisienne", cursive; font-size: 29px; color: var(--tagline-blue);
    white-space: nowrap;
  }
  .main-nav {
    position: absolute; left: 0; top: 122px; width: 1075px; height: 38px;
    background: var(--brand-blue);
    display: flex; padding-left: 92px;
  }
  .main-nav a {
    color: var(--white); text-decoration: none; font-size: 11.5px;
    line-height: 38px; padding: 0 26px 0 17px;
    border-right: 1px solid rgba(255,255,255,0.25);
    white-space: nowrap;
  }
  .main-nav a:last-child { border-right: none; }
  .hero {
    position: absolute; left: 0; top: 160px; width: 1075px; height: 503px;
    background: linear-gradient(#dfe7f2, #eef2f8 80%, #f7f9fc);
  }
  .hero-frame {
    position: absolute; left: 94px; top: 33px; width: 891px; height: 405px;
    background: var(--white); padding: 6px;
    box-shadow: 0 22px 24px -14px rgba(0,0,0,0.35);
  }
  .hero-slide {
    width: 100%; height: 100%;
    background: linear-gradient(135deg, #6d6d6d, #b6b6b6 45%, #585858 75%, #2a2a2a);
  }
  .mission-title {
    position: absolute; left: 93px; top: 690px;
    font-family: "Cabin", sans-serif; font-weight: 500; font-size: 27px;
    color: var(--brand-blue); letter-spacing: 0.5px;
  }
  .mission-rule { position: absolute; left: 97px; top: 731px; width: 871px; height: 1px; background: var(--rule); }
  .mission-rule-accent { position: absolute; left: 97px; top: 730px; width: 146px; height: 4px; background: var(--rule); }
  .mission-photo {
    position: absolute; left: 97px; top: 758px; width: 187px; height: 229px;
    background: var(--white); border: 1px solid #e4e4e4; padding: 3px;
  }
  .mission-photo div { width: 100%; height: 100%; background: linear-gradient(#b9c6d4, #c8675d 55%, #d8d8dc); }
  .mission-copy { position: absolute; left: 297px; top: 755px; width: 676px; }
  .mission-copy h2 {
    font-family: "Libre Baskerville", serif; font-weight: 400; font-size: 19px;
    line-height: 27px; color: #3a3a3a; margin-bottom: 15px;
  }
  .mission-copy p { font-size: 12px; line-height: 18px; color: #3a3a3a; margin-bottom: 18px; }
  .read-more {
    position: absolute; left: 297px; top: 960px; width: 92px; height: 28px;
    background: var(--brand-blue); border-radius: 3px; color: var(--white);
    font-family: "Cabin", sans-serif; font-size: 14px; text-align: center; line-height: 28px;
    box-shadow: 0 2px 0 #23588a;
  }
  .site-footer {
    position: absolute; left: 0; top: 1058px; width: 1075px; height: 142px;
    background: linear-gradient(var(--footer-bg) 0, var(--footer-bg) 107px, var(--footer-base) 107px);
  }
  .footer-brand {
    position: absolute; left: 91px; top: 43px;
    font-family: "Cabin", sans-serif; font-weight: 500; font-size: 17px; color: #d6d6d6;
    display: flex; align-items: center; gap: 8px; white-space: nowrap;
  }
  .footer-brand span { width: 12px; height: 12px; border-radius: 50%; background: #8a8a8a; }
  .footer-links { position: absolute; top: 11px; list-style: none; }
  .footer-links li {
    font-size: 10px; line-height: 19.7px; color: var(--footer-text); letter-spacing: 0.5px;
    padding-left: 14px; position: relative;
  }
  .footer-links li::before { content: "•"; position: absolute; left: 0; color: #888; }
  .links-products { left: 327px; }
  .links-company { left: 587px; }
  .phone-icon { position: absolute; left: 760px; top: 12px; }
  .help-line {
    position: absolute; left: 790px; top: 10px; width: 142px; text-align: center;
    color: #dcdcdc; font-weight: bold; font-size: 10px; line-height: 19px; letter-spacing: 0.5px;
  }
  .help-line .phone-number { font-size: 11px; color: var(--white); }
  .help-email {
    position: absolute; left: 770px; top: 85px; width: 185px; text-align: center;
    color: var(--white); font-weight: bold; font-size: 11px;
  }
</style>
</head>
<body>
  <header class="site-header">
    <div class="brand"><span class="brand-dot"></span>Brightwave Youth Academy</div>
    <div class="tagline">Nurture Global Citizens and Global Leaders</div>
  </header>

  <nav class="main-nav">
    <a href="#">HOME</a>
    <a href="#">HARLOW SUMMER PROGRAM</a>
    <a href="#">LAKEVIEW SUMMER CAMP</a>
    <a href="#">WHOLE YEAR PROGRAM</a>
    <a href="#">KESTREL UNIVERSITY</a>
  </nav>

  <section class="hero" role="img" aria-label="Faint background collage of paired student photos">
    <div class="hero-frame">
      <div class="hero-slide" role="img" aria-label="Photo slider: black and white collage of students at summer program activities"></div>
    </div>
  </section>

  <h1 class="mission-title">Our Mission</h1>
  <div class="mission-rule"></div>
  <div class="mission-rule-accent"></div>

  <div class="mission-photo">
    <div role="img" aria-label="Two paired students wearing Chinese and American flags on a city rooftop"></div>
  </div>

  <section class="mission-copy">
    <h2>Brightwave Youth Academy is to help American students and Chinese students to break the barriers between the two different cultures</h2>
    <p>Brightwave Youth Academy is to help American students and Chinese students to break the barriers between the two different cultures, experiences and education backgrounds by providing a global summer program in the U.S. with American students and Chinese students one to one paired, home stay in US families, intensive learning and culture adventure activities, and get them fully prepared for their college education and career developments in this interdependent world.</p>
    <p>Phasellus tempor enim purus, vitae venenatis est. Ut imperdiet hendrerit pulvinar. Cras at tellus a enim condimentum mollis ut et tellus. Mauris dolor magna, elementum eu dictum eu, fermentum a nibh. Praesent ut dui lectus.</p>
  </section>
  <a class="read-more" href="#">Read More</a>

  <footer class="site-footer">
    <div class="footer-brand"><span></span>Brightwave Youth Academy</div>
    <ul class="footer-links links-products">
      <li>Mara's Raw Food Essentials</li>
      <li>Mara's Raw Food Desserts</li>
      <li>Mara's Raw Food Kitchen</li>
      <li>Mara's Ready Mixes</li>
      <li>Desserts</li>
    </ul>
    <ul class="footer-links links-company">
      <li>About</li>
      <li>Services</li>
      <li>Wellness Education</li>
      <li>Schedule a Consult</li>
      <li>Store</li>
    </ul>
    <svg class="phone-icon" width="50" height="62" viewBox="0 0 50 62" aria-hidden="true">
      <path d="M8 4 L18 2 L22 16 L15 20 Q18 34 28 44 L35 40 L44 50 L38 58 Q14 52 4 14 Z" fill="var(--phone-orange)"/>
      <ellipse cx="30" cy="58" rx="14" ry="3" fill="#111"/>
    </svg>
    <div class="help-line">
      24/7 HELP LINE<br>
      <span class="phone-number">(555) 014 - 2287</span><br>
      OR<br>
      ONLINE HELP
    </div>
    <div class="help-email">hello@brightwaveyouth.org</div>
  </footer>
</body>
</html>
```